WordPress Site That Reviews Footwear

We need a wordpress web design for an affiliate site called TreadNest. We review and do roundups on footwear products. The final design should be clean and mobile friendly. The site should be built with Gutenberg page builder. We like the design of https://dermalquill.com/.
Updates

Need extra days to review

Target Market(s)

USA

Industry/Entity Type

Footwear

Logo Text

TreadNest

Number of Pages Required

4 page

Font styles to use
Serif
Sans Serif

Requirements
Must have
• Wordpress site
Blog post
Page
Categories
Homepage

```html
<!DOCTYPE html>
<html lang="en">
<head>
<meta charset="utf-8">
<title>TreadNest — Footwear Reviews</title>
<link href="https://fonts.googleapis.com/css2?family=Poppins:ital,wght@0,300;0,400;0,500;0,600;0,700;0,800;1,300&family=Yellowtail&display=swap" rel="stylesheet">
<style>
:root{
  --hero-pink:#c94f78;
  --hero-purple:#7a2fd8;
  --accent:#6a2cc6;
  --accent-ring:#7b35c9;
  --rose:#c54b80;
  --sky:#6ea6dc;
  --ink:#111111;
  --body:#3a3a3a;
  --muted:#8a8a8a;
  --band:#2a2a2c;
  --band-hi:#7f9aa3;
  --footer:#1f102f;
  --white:#ffffff;
}
*{margin:0;padding:0;box-sizing:border-box}
html,body{width:1200px;height:3604px;overflow:hidden}
body{position:relative;font-family:'Poppins',sans-serif;background:var(--white);color:var(--ink)}
.abs{position:absolute}

/* hero */
.hero{left:0;top:0;width:1200px;height:624px;background:linear-gradient(100deg,var(--hero-pink) 0%,#a53fa6 45%,var(--hero-purple) 100%)}
.logo{font-weight:700;color:var(--white);font-size:28px;letter-spacing:.2px}
.nav{left:436px;top:46px;display:flex;gap:29px;font-size:14px;color:var(--white)}
.nav a{color:var(--white);text-decoration:none}
.nav .current{font-weight:600}
.social{display:flex;gap:22px}
.social span{display:block;width:16px;height:16px;border-radius:50%;background:var(--white)}
.hero h1{left:155px;top:190px;font-size:49px;line-height:53px;font-weight:800;color:var(--white)}
.hero p{left:157px;top:314px;width:460px;font-size:14.5px;line-height:26px;color:var(--white)}
.btn-outline{left:157px;top:422px;width:243px;height:50px;border:1.5px solid var(--white);color:var(--white);font-size:13px;font-weight:500;display:flex;align-items:center;justify-content:center;letter-spacing:.3px}
.hero-boot{left:640px;top:140px;width:400px;height:360px;border-radius:40% 45% 30% 35%;background:radial-gradient(ellipse at 50% 45%,#a8643a 0%,#7a4424 55%,rgba(90,40,30,0) 75%)}

/* category cards */
.card{overflow:hidden}
.card-women{left:158px;top:708px;width:276px;height:369px;background:linear-gradient(180deg,#6f6fc4 0%,#8b5aa6 55%,#7c4a74 100%)}
.card-mountain{left:463px;top:708px;width:276px;height:369px;background:linear-gradient(180deg,#4b5e78 0%,#8896a8 40%,#3f4a45 100%)}
.card-winter{left:767px;top:708px;width:275px;height:170px;background:linear-gradient(135deg,#c6b3ea 0%,#9a7ed6 55%,#d14b9a 100%)}
.card-best{left:767px;top:906px;width:275px;height:171px;background:var(--rose);color:var(--white);text-align:center}
.card .kicker{font-size:17px;font-weight:300;color:var(--white)}
.card .big{font-size:24px;line-height:27px;font-weight:700;color:var(--white)}
.card-women .label{position:absolute;left:37px;top:36px}
.card-mountain .label{position:absolute;left:0;width:100%;top:197px;text-align:center}
.btn-small{display:inline-block;margin-top:20px;border:1.5px solid var(--white);padding:7px 17px;font-size:13.5px;color:var(--white)}
.script{font-family:'Yellowtail',cursive;font-size:25px;color:var(--white)}
.card-winter .script{position:absolute;width:100%;text-align:center;top:66px}
.card-best .script{margin-top:24px;display:block}
.card-best .note{font-size:11.5px;font-style:italic;font-weight:300;line-height:19px;width:200px;margin:8px auto 0}
.stars{margin-top:6px;font-size:10px;letter-spacing:2px}

/* purpose */
.purpose-photo{left:0;top:1168px;width:538px;height:611px;background:var(--sky)}
.purpose-boot{left:70px;top:1240px;width:510px;height:440px;border-radius:45% 40% 35% 45%;background:radial-gradient(ellipse at 55% 50%,#6e6558 0%,#4a4540 50%,rgba(60,60,60,0) 72%)}
.purpose h2{left:625px;top:1210px;font-size:43px;line-height:52px;font-weight:800;color:var(--ink)}
.feature .ring{position:absolute;left:-1px;width:96px;height:96px;border-radius:50%;border:5px solid var(--accent-ring);display:flex;align-items:center;justify-content:center}
.feature h3{position:absolute;left:112px;font-size:20px;font-weight:600;color:var(--accent)}
.feature p{position:absolute;left:112px;width:290px;font-size:13.5px;line-height:22px;color:var(--body)}

/* dark band */
.band{left:0;top:1868px;width:1200px;height:663px;background:radial-gradient(ellipse at 55% 60%,#4d4a44 0%,#2b2b2c 50%,#1d1d1e 100%)}
.band-col{position:absolute;top:0;width:240px;height:663px;border-right:1px solid rgba(255,255,255,.25);text-align:center;color:var(--white)}
.band-col:last-child{border-right:none}
.band-col .hi{position:absolute;left:0;top:0;width:100%;height:240px;background:var(--band-hi);opacity:.85}
.band-col h4{position:relative;margin-top:82px;font-size:23px;line-height:29px;font-weight:700}
.band-col p{position:relative;margin:14px auto 0;width:200px;font-size:13px;line-height:23px;font-weight:400;opacity:.92}

/* experts */
.experts h2{left:0;width:1200px;top:2598px;text-align:center;font-size:44px;font-weight:800}
.experts .intro{left:0;width:1200px;top:2668px;text-align:center;font-size:14.5px;line-height:26px;color:var(--body)}
.post{width:274px;height:294px;background:var(--white);box-shadow:0 6px 22px rgba(0,0,0,.06)}
.post .thumb{position:relative;height:173px}
.post .date{position:absolute;left:4px;top:26px;width:20px;height:96px;background:var(--white);display:flex;align-items:center;justify-content:center}
.post .date span{transform:rotate(-90deg);white-space:nowrap;font-size:10px;font-weight:600;color:var(--accent)}
.post h5{margin:20px 0 0 31px;font-size:16.5px;line-height:21px;font-weight:700}
.post .more{margin:10px 0 0 31px;font-size:12.5px;font-weight:600;color:var(--accent);display:flex;align-items:center;gap:6px}
.dots{left:580px;top:3080px;display:flex;gap:8px}
.dots span{width:7px;height:7px;border-radius:50%;background:#e0dcc8}
.dots .on{background:var(--accent)}

/* footer */
.footer{left:0;top:3176px;width:1200px;height:428px;background:var(--footer);color:var(--white)}
.footer h6{position:absolute;font-size:15px;font-weight:400;letter-spacing:.5px}
.footer ul{position:absolute;list-style:none;font-size:13.5px;line-height:20px}
.footer .money{position:absolute;left:347px;top:126px;width:250px;font-size:13px;line-height:25px}
.copyright{position:absolute;left:0;width:1200px;top:392px;text-align:center;font-size:11px;opacity:.85}
</style>
</head>
<body>

<header class="abs hero">
  <div class="abs logo" style="left:157px;top:38px">TreadNest</div>
  <nav class="abs nav">
    <a class="current">Home</a><a>Info</a><a>Boots</a><a>Shoes</a><a>Gear</a><a>Footwear</a><a>Sports</a>
  </nav>
  <div class="abs social" style="left:948px;top:47px" aria-label="Social links"><span></span><span></span><span></span></div>
  <h1 class="abs">Make Your<br>Shoes Shine Again</h1>
  <p class="abs">Lorem ipsum dolor sit amet, consectetur adipiscing elit, sed do eiusmod tempor incididunt ut labore et dolore magna aliqua. Ut enim ad minim veniam</p>
  <div class="abs btn-outline">CHECK OUT OUR FAVORITES</div>
  <div class="abs hero-boot" role="img" aria-label="Photo of a tan leather lace-up work boot"></div>
</header>

<section class="categories">
  <div class="abs card card-women" role="img" aria-label="Photo of a hiker's legs in boots on a rocky summit">
    <div class="label"><div class="kicker">The Top 20 Best</div><div class="big">Women's Hiking<br>Boots</div></div>
  </div>
  <div class="abs card card-mountain" role="img" aria-label="Photo of a mountaineering boot against snowy peaks">
    <div class="label"><div class="kicker">Top 25 Men</div><div class="big">Mountaineering<br>Boots</div><span class="btn-small">View Products</span></div>
  </div>
  <div class="abs card card-winter" role="img" aria-label="Photo of a winter boot stepping into snow">
    <div class="script">Winter Hiking Boots</div>
  </div>
  <div class="abs card card-best">
    <span class="script">Best Hiking Boots</span>
    <p class="note">When temperatures drop, some people use this as an excuse to remain indoors.</p>
    <div class="stars">☆☆☆☆☆</div>
  </div>
</section>

<section class="purpose">
  <div class="abs purpose-photo"></div>
  <div class="abs purpose-boot" role="img" aria-label="Photo of a pair of brown hiking boots"></div>
  <h2 class="abs">What's Your Boot<br>Purpose</h2>

  <div class="abs feature" style="left:633px;top:1357px;width:420px;height:110px">
    <div class="ring" style="top:0">
      <svg width="46" height="46" viewBox="0 0 46 46" fill="none" stroke="#222" stroke-width="2" stroke-linecap="round" stroke-linejoin="round"><path d="M6 28l10-10 7 4 6-6 11 11-10 10-7-4-6 6z"/><path d="M16 18l8 8M22 14v-5M15 11l-2-3M29 11l2-3"/></svg>
    </div>
    <h3 style="top:0">Great support</h3>
    <p style="top:36px">Lorem ipsum dolor sit amet, consectetur adipiscing elit, sed do eiusmod tempor incididunt ut labore et...</p>
  </div>

  <div class="abs feature" style="left:633px;top:1494px;width:420px;height:110px">
    <div class="ring" style="top:0">
      <svg width="46" height="46" viewBox="0 0 46 46" fill="none" stroke="#222" stroke-width="2" stroke-linecap="round" stroke-linejoin="round"><path d="M10 40V14M5 19l5-5 5 5M36 40V14M31 19l5-5 5 5"/><path d="M17 26v-9h12v9l-3 5h-6z"/><path d="M20 17v-4M23 17v-5M26 17v-4"/></svg>
    </div>
    <h3 style="top:0">Sturdy Construction</h3>
    <p style="top:36px">Lorem ipsum dolor sit amet, consectetur adipiscing elit, sed do eiusmod tempor incididunt ut labore et...</p>
  </div>

  <div class="abs feature" style="left:633px;top:1636px;width:420px;height:110px">
    <div class="ring" style="top:0">
      <svg width="46" height="46" viewBox="0 0 46 46" fill="none" stroke="#222" stroke-width="2" stroke-linecap="round" stroke-linejoin="round"><ellipse cx="15" cy="22" rx="8" ry="15"/><ellipse cx="31" cy="22" rx="8" ry="15"/><path d="M9 20h12M25 20h12"/></svg>
    </div>
    <h3 style="top:0">Comfortable</h3>
    <p style="top:36px">Lorem ipsum dolor sit amet, consectetur adipiscing elit, sed do eiusmod tempor incididunt ut labore et...</p>
  </div>
</section>

<section class="abs band" role="img" aria-label="Photo of a pair of cream canvas boots on a dark background">
  <div class="band-col" style="left:0"><h4>Sed Ut<br>Perspiciatis</h4><p>Lorem ipsum dolor sit amet, consectetur adipisc rngelit sed do</p></div>
  <div class="band-col" style="left:240px"><h4>Sed Ut<br>Perspiciatis</h4><p>Lorem ipsum dolor sit amet, consectetur adipisc rngelit sed do</p></div>
  <div class="band-col" style="left:480px"><div class="hi"></div><h4>Sed Ut<br>Perspiciatis</h4><p>Lorem ipsum dolor sit amet, consectetur adipisc rngelit sed do</p></div>
  <div class="band-col" style="left:720px"><h4>Sed Ut<br>Perspiciatis</h4><p>Lorem ipsum dolor sit amet, consectetur adipisc rngelit sed do</p></div>
  <div class="band-col" style="left:960px"><h4>Sed Ut<br>Perspiciatis</h4><p>Lorem ipsum dolor sit amet, consectetur adipisc rngelit sed do</p></div>
</section>

<section class="experts">
  <h2 class="abs">Learn from the experts.</h2>
  <p class="abs intro">Lorem ipsum dolor sit amet, consectetur adipiscing elit, sed do eiusmod tempor incididunt ut<br>labore et dolore magna aliqua. Ut enim ad minim veniam</p>

  <article class="abs post" style="left:158px;top:2751px">
    <div class="thumb" role="img" aria-label="Photo of boots with crampons on snow" style="background:linear-gradient(135deg,#2e4f8e 0%,#d49a2a 45%,#eef3f8 100%)">
      <div class="date"><span>May 19, 20221</span></div>
    </div>
    <h5>Lorem ipsum dolor sit<br>amt conse ctetur adipis,</h5>
    <div class="more">Learn More <svg width="14" height="10" viewBox="0 0 14 10" fill="none" stroke="currentColor" stroke-width="1.5"><path d="M0 5h12M8 1l4 4-4 4"/></svg></div>
  </article>

  <article class="abs post" style="left:468px;top:2751px">
    <div class="thumb" role="img" aria-label="Photo of a climber on a snowy ridge at dusk" style="background:linear-gradient(180deg,#3a2d7a 0%,#7f69c4 55%,#d8d2ee 100%)">
      <div class="date"><span>May 19, 20221</span></div>
    </div>
    <h5>Lorem ipsum dolor sit<br>amt conse ctetur adipis,</h5>
    <div class="more">Learn More <svg width="14" height="10" viewBox="0 0 14 10" fill="none" stroke="currentColor" stroke-width="1.5"><path d="M0 5h12M8 1l4 4-4 4"/></svg></div>
  </article>

  <article class="abs post" style="left:768px;top:2751px">
    <div class="thumb" role="img" aria-label="Photo of hiking boots on a rocky trail" style="background:linear-gradient(180deg,#8fa7b8 0%,#6a6a4a 50%,#4d3a2a 100%)">
      <div class="date"><span>May 19, 20221</span></div>
    </div>
    <h5>Lorem ipsum dolor sit<br>amt conse ctetur adipis,</h5>
    <div class="more">Learn More <svg width="14" height="10" viewBox="0 0 14 10" fill="none" stroke="currentColor" stroke-width="1.5"><path d="M0 5h12M8 1l4 4-4 4"/></svg></div>
  </article>

  <div class="abs dots"><span></span><span class="on"></span><span></span></div>
</section>

<footer class="abs footer">
  <div class="abs logo" style="left:126px;top:136px">TreadNest</div>
  <h6 style="left:347px;top:88px">HOW WE MAKE MONEY</h6>
  <p class="money">Lorem ipsum dolor sit amet, conse tetur adipiscing elit, sed do eiusmod tempor incididunt ut labore et dolormagna aliqua.</p>
  <div class="abs social" style="left:351px;top:276px" aria-label="Social links"><span></span><span></span><span></span></div>

  <h6 style="left:660px;top:88px">ABOUT</h6>
  <ul style="left:660px;top:132px"><li style="margin-bottom:14px">About</li><li style="margin-bottom:14px">Contact</li><li>Media</li></ul>

  <h6 style="left:797px;top:86px">COMPANY</h6>
  <ul style="left:797px;top:130px;width:140px"><li style="margin-bottom:21px">Terms of Use</li><li style="margin-bottom:21px">Privacy Policy</li><li style="margin-bottom:21px">Editorial Policy</li><li>How We Make<br>Money</li></ul>

  <h6 style="left:982px;top:86px">DISCOVER</h6>
  <ul style="left:982px;top:130px"><li style="margin-bottom:21px">Products</li><li style="margin-bottom:21px">Skin Type</li><li style="margin-bottom:21px">Skin Concerns</li><li>Reviews</li></ul>

  <div class="copyright">© Copyright TreadNest All rights reserved.</div>
</footer>

</body>
</html>
```